Landing page design for soccer portal (Working html + css + images)

We need a design for a landing page for a new soccer portal where the audience is both players and trainers.
The landing page should have the following required elements:
- Short explanation for players. (Players will have to download App in appstore/playstore)
- Short explanations for trainers (will use web site)
- Short explanation for Clubs (Will use web site)
- Login/Signup buttons
Audience to attract:
Boys/Girls 10 - 17 years
Soccer trainers.
What we like:
Usage of cool/professional background images.
Animating/Parallaxing text
Inspirational landing pages:
https://www.qorvalplay.com/brento
We need the following assets as the output of the design:
- working html + css + image files
- The images used in the landing page needs to be royalty free (or not too expensive)
Soccerplayers (age 10-17)
Soccer trainers

```html
<!DOCTYPE html>
<html lang="en">
<head>
<meta charset="utf-8">
<title>Kickline Arena – Soccer Portal</title>
<link rel="stylesheet" href="https://fonts.googleapis.com/css2?family=Barlow+Condensed:wght@500;600;700&family=Open+Sans:wght@400;600&family=Montserrat:wght@500&display=swap">
<style>
:root{
  --yellow:#ffdb1a;
  --ink:#141414;
  --white:#ffffff;
  --grey:#6d6d6d;
  --line:#d9d9d9;
  --field-border:#6b5b10;
  --dark:#0d1017;
}
*{margin:0;padding:0;box-sizing:border-box}
html,body{width:1200px;height:2632px;overflow:hidden}
body{position:relative;background:var(--white);font-family:"Open Sans",Arial,sans-serif;color:var(--ink)}
.abs{position:absolute}
.heading{font-family:"Barlow Condensed","Arial Narrow",sans-serif;font-weight:600;text-transform:uppercase;letter-spacing:.5px}
.btn{position:absolute;display:flex;align-items:center;justify-content:center;border-radius:20px;font-family:"Barlow Condensed","Arial Narrow",sans-serif;font-weight:600;font-size:12.5px;text-transform:uppercase;letter-spacing:.3px}
.btn-yellow{background:var(--yellow);color:var(--ink)}
.btn-ghost-light{border:1.5px solid var(--white);color:var(--white)}
.btn-ghost-dark{border:1.5px solid var(--ink);color:var(--ink)}
.copy p{font-size:12px;line-height:23.5px;margin-bottom:12px}

/* hero */
.hero{left:0;top:0;width:1200px;height:558px;background:radial-gradient(ellipse at 60% 30%,#9aa09a 0%,#4d5550 35%,#25302a 70%,#1a2a18 100%)}
.hero-shade{left:0;top:0;width:1200px;height:558px;background:linear-gradient(180deg,rgba(0,0,0,.25),rgba(0,0,0,.05) 50%,rgba(20,40,10,.4))}
.brand{left:132px;top:33px;font-family:"Barlow Condensed","Arial Narrow",sans-serif;font-weight:600;font-size:29px;color:var(--yellow);text-transform:uppercase;letter-spacing:.5px}
.nav{left:506px;top:40px;display:flex;gap:0}
.nav a{font-family:"Barlow Condensed","Arial Narrow",sans-serif;font-weight:600;font-size:12.5px;color:var(--white);text-decoration:none;text-transform:uppercase;margin-right:38px}
.hero-title{left:0;width:1200px;top:220px;text-align:center;font-size:62px;color:var(--white)}
.hero-sub{left:0;width:1200px;top:290px;text-align:center;font-family:"Montserrat",Arial,sans-serif;font-weight:500;font-size:13.5px;line-height:25px;color:var(--white)}

/* players */
.players{left:0;top:558px;width:1200px;height:533px;background:var(--yellow)}
.store-badge{position:absolute;top:305px;height:53px;border-radius:7px;background:#111;border:1.5px solid #777;display:flex;align-items:center;justify-content:center;gap:10px;color:var(--white);font-family:"Open Sans",Arial,sans-serif;font-weight:600;font-size:19px}
.store-badge i{width:14px;height:14px;border-radius:50%;background:var(--white);display:block}

/* trainers */
.trainers{left:0;top:1091px;width:1200px;height:458px;background:linear-gradient(90deg,#07090e 0%,#0f141c 40%,#2a3440 62%,#1c2430 80%,#0c1016 100%)}
.trainers .copy{color:var(--white)}

/* clubs */
.clubs{left:0;top:1549px;width:1200px;height:411px;background:var(--white)}
.club-grid{left:132px;top:82px;width:421px;height:246px;display:grid;grid-template-columns:repeat(3,1fr);grid-template-rows:repeat(2,1fr)}
.club-cell{display:flex;align-items:center;justify-content:center;font-family:"Open Sans",Arial,sans-serif;font-weight:600;font-size:19px;color:#7a7a7a}
.club-cell:nth-child(-n+3){border-bottom:1px solid var(--line)}
.club-cell:nth-child(3n+1),.club-cell:nth-child(3n+2){border-right:1px solid var(--line)}
.clubs .copy{color:var(--grey)}

/* newsletter */
.newsletter{left:0;top:1960px;width:1200px;height:577px;background:var(--yellow)}
.field{position:absolute;border:1px solid var(--field-border);font-size:12px;padding:8px 12px;color:#3a3a3a}
.divider{left:132px;top:433px;width:936px;border-top:1px dashed #c9ab08}
.social{position:absolute;top:462px;width:120px;text-align:center;font-family:"Barlow Condensed","Arial Narrow",sans-serif;font-weight:600;font-size:13px;text-transform:uppercase}
.social i{display:block;width:16px;height:16px;border-radius:50%;background:var(--ink);margin:0 auto 10px}

/* footer */
.footer{left:0;top:2537px;width:1200px;height:95px;background:var(--white);text-align:center}
.footer-links{margin-top:26px;font-size:11px;color:#333;text-transform:uppercase}
.footer-links span{margin:0 16px;color:#777}
.copyright{margin-top:10px;font-size:10.5px;color:#444;text-transform:uppercase}
</style>
</head>
<body>

<header class="abs hero" role="img" aria-label="Stadium photo of a soccer player striking a ball under floodlights"></header>
<div class="abs hero-shade"></div>
<div class="abs brand">Kickline Arena</div>
<nav class="abs nav">
  <a href="#">Home</a><a href="#">About us</a><a href="#">Players</a><a href="#">Trainers</a><a href="#">Clubs</a><a href="#">Contacts</a>
</nav>
<a class="btn btn-yellow" style="left:961px;top:32px;width:106px;height:35px">Login / Signup</a>
<svg class="abs" style="left:110px;top:240px" width="24" height="96" viewBox="0 0 24 96"><polyline points="22,2 2,48 22,94" fill="none" stroke="#fff" stroke-opacity=".6" stroke-width="1.5"/></svg>
<svg class="abs" style="left:1066px;top:240px" width="24" height="96" viewBox="0 0 24 96"><polyline points="2,2 22,48 2,94" fill="none" stroke="#fff" stroke-opacity=".6" stroke-width="1.5"/></svg>
<h1 class="abs heading hero-title">Soccer Portal</h1>
<p class="abs hero-sub">Aliquip ex ea commodo consequat. Duis aute irure dolor in reprehenderit in voluptate<br>dolore eu fugiat nulla pariatur occaecat cupidatat.</p>
<a class="btn btn-yellow" style="left:474px;top:363px;width:122px;height:37px">Learn more info</a>
<a class="btn btn-ghost-light" style="left:602px;top:363px;width:122px;height:37px">Get started today</a>
<svg class="abs" style="left:586px;top:466px" width="28" height="50" viewBox="0 0 28 50"><rect x="1" y="1" width="26" height="48" rx="13" fill="none" stroke="#fff" stroke-opacity=".7" stroke-width="1.2"/><circle cx="14" cy="20" r="2.5" fill="#fff"/></svg>

<section class="abs players">
  <div class="abs" style="left:132px;top:39px;width:429px;height:494px;background:radial-gradient(ellipse at 55% 45%,#c8201e 0%,#b4402a 30%,#f0a52a 60%,rgba(255,219,26,0) 80%)" role="img" aria-label="Photo of a young soccer player in a red shirt kicking a ball"></div>
  <div class="abs copy" style="left:632px;top:95px;width:440px">
    <h2 class="heading" style="font-size:39px;margin-bottom:16px">Players</h2>
    <p>Adipiscing elit, sed do eiusmod tempor incididunt ut labore et dolore magna aliqua. Ut enim ad minim veniam, quis nostrud exercitation ullamco laboris nisi ut aliquip ex ea commodo consequat proident</p>
    <p>Enim ad minim veniam, quis nostrud exercitation ullamco laboris nisi ut aliquip ex ea commodo consequat proident...</p>
  </div>
  <div class="store-badge" style="left:632px;width:163px"><i></i>Playbox</div>
  <div class="store-badge" style="left:803px;width:164px"><i></i>Appvault</div>
  <a class="btn btn-ghost-dark" style="left:632px;top:384px;width:126px;height:39px">Download apps</a>
</section>

<section class="abs trainers" role="img" aria-label="Night stadium photo of two soccer players competing for the ball">
  <div class="abs copy" style="left:132px;top:90px;width:440px">
    <h2 class="heading" style="font-size:39px;margin-bottom:16px">Trainers</h2>
    <p>Adipiscing elit, sed do eiusmod tempor incididunt ut labore et dolore magna aliqua. Ut enim ad minim veniam, quis nostrud exercitation ullamco laboris nisi ut aliquip ex ea commodo consequat proident</p>
    <p>Enim ad minim veniam, quis nostrud exercitation ullamco laboris nisi ut aliquip ex ea commodo consequat proident...</p>
  </div>
  <a class="btn btn-yellow" style="left:132px;top:316px;width:122px;height:38px">Learn more info</a>
  <a class="btn btn-ghost-light" style="left:263px;top:316px;width:125px;height:38px">Start your training</a>
</section>

<section class="abs clubs">
  <div class="abs club-grid">
    <div class="club-cell">Marlow</div>
    <div class="club-cell">Lutece Mode</div>
    <div class="club-cell">Verdant &amp; Co</div>
    <div class="club-cell">Holt Ember</div>
    <div class="club-cell">Wellfold</div>
    <div class="club-cell">Rosk</div>
  </div>
  <div class="abs copy" style="left:632px;top:80px;width:440px">
    <h2 class="heading" style="font-size:39px;margin-bottom:16px;color:var(--ink)">Clubs</h2>
    <p>Adipiscing elit, sed do eiusmod tempor incididunt ut labore et dolore magna aliqua. Ut enim ad minim veniam, quis nostrud exercitation ullamco laboris nisi ut aliquip ex ea commodo consequat proident</p>
    <p>Enim ad minim veniam, quis nostrud exercitation ullamco laboris nisi ut aliquip ex ea commodo consequat proident...</p>
  </div>
  <a class="btn btn-yellow" style="left:632px;top:289px;width:123px;height:37px">View more info</a>
</section>

<section class="abs newsletter">
  <h2 class="abs heading" style="left:0;width:1200px;top:56px;text-align:center;font-size:33px">Newsletter</h2>
  <p class="abs" style="left:200px;width:800px;top:100px;text-align:center;font-size:12px;line-height:23px">Adipiscing elit, sed do eiusmod tempor incididunt ut labore et dolore magna aliqua. Ut enim ad minim veniam, quis nostrud exercitation ullamco laboris nisi ut aliquip ex ea commodo consequat proident</p>
  <div class="field" style="left:261px;top:171px;width:285px;height:35px">Name*</div>
  <div class="field" style="left:261px;top:213px;width:285px;height:35px">Email*</div>
  <div class="field" style="left:261px;top:255px;width:285px;height:35px">Phone*</div>
  <div class="field" style="left:261px;top:297px;width:285px;height:35px">Address*</div>
  <div class="field" style="left:558px;top:171px;width:381px;height:160px">Comments*</div>
  <a class="btn btn-ghost-dark" style="left:537px;top:357px;width:124px;height:39px">Submit here</a>
  <div class="abs divider"></div>
  <div class="social" style="left:296px"><i></i>Friendwall</div>
  <div class="social" style="left:456px"><i></i>Chirper</div>
  <div class="social" style="left:621px"><i></i>Clipstream</div>
  <div class="social" style="left:779px"><i></i>Snapgrid</div>
</section>

<footer class="abs footer">
  <div class="footer-links">Home<span>|</span>About us<span>|</span>Players<span>|</span>Trainers<span>|</span>Clubs<span>|</span>Contacts</div>
  <div class="copyright">Copyrights © Kickline Arena . 2017 | All rights reserved.</div>
</footer>

</body>
</html>
```